TWR Handyman Service

File 2 Prep kitchen cabinets
File 3 Painting kitchen cabinets
File 4 Demo stairs
File 5 Completion Installing stair treads
File 6 Power washing deck
File 7 Completion of Sainting deck and railings
File 8 Completion of staining steps
Logo, owner name, email and web site on front cover
File 9 Demo living room floor
File 10 Completion of living room floor
Please see additional on attached flyer

Target Market(s)

Residential

Industry/Entity Type

Painting

Font styles to use
Serif
Sans Serif

Requirements
Must have
• Some Photos and type of work discerption
Front page Logo, web address, phone number, owners name and email address
Back Page see attached file 1
Nice to have
• Photo maybe in middle of flyer
Use the best text that you think will meet the needs
Should not have
• No pink colors

```html
<!DOCTYPE html>
<html lang="en">
<head>
<meta charset="utf-8">
<title>TWR Handyman Services – Trifold Outside</title>
<link href="https://fonts.googleapis.com/css2?family=Montserrat:wght@600;800;900&family=Oswald:wght@600;700&family=Open+Sans:wght@400;600;700&display=swap" rel="stylesheet">
<style>
  :root{
    --navy:#25337a;
    --navy-deep:#1d2866;
    --gold:#d8b06c;
    --gold-light:#e6c488;
    --gold-dark:#c89a52;
    --white:#ffffff;
    --paper:#f2f2f2;
    --photo-wood:#8a6a4e;
    --photo-wall:#e9e6e0;
    --photo-grey:#cfcfcf;
  }
  *{margin:0;padding:0;box-sizing:border-box}
  html,body{width:1200px;height:800px;overflow:hidden;background:#3a3a3a}
  .brochure{position:relative;width:1200px;height:800px;overflow:hidden;font-family:"Open Sans",sans-serif}
  .panel-shapes{position:absolute;inset:0}
  .abs{position:absolute}

  /* Left panel */
  .headline{left:36px;top:468px;font-family:"Montserrat",sans-serif;font-weight:900;font-size:44px;line-height:48px;text-transform:uppercase}
  .headline .w{color:var(--white)}
  .headline .n{color:var(--navy)}
  .perks{left:40px;top:668px;list-style:none}
  .perks li{width:300px;height:22px;margin-bottom:4px;padding-left:14px;font-family:"Open Sans",sans-serif;font-weight:700;font-size:15px;line-height:22px;color:var(--navy);
    background:linear-gradient(90deg,var(--white) 0%,rgba(255,255,255,.85) 45%,rgba(255,255,255,0) 100%)}

  /* Middle panel */
  .call{left:400px;width:400px;top:282px;text-align:center;font-family:"Montserrat",sans-serif;font-weight:900;color:var(--white);text-transform:uppercase}
  .call .l1{font-size:42px;line-height:44px}
  .call .l2{font-size:34px;line-height:38px}
  .phone-bar{left:450px;top:392px;width:300px;height:46px;background:var(--white);border-radius:6px;text-align:center;font-family:"Montserrat",sans-serif;font-weight:800;font-size:34px;line-height:46px;color:var(--navy)}
  .brand-mark{left:400px;width:400px;top:478px;display:flex;align-items:center;justify-content:center;gap:10px}
  .brand-mark .sq{width:30px;height:30px;border:4px solid var(--white)}
  .brand-mark .name{font-family:"Open Sans",sans-serif;font-weight:700;font-size:20px;color:var(--white)}
  .ribbon{left:438px;top:540px;width:324px;height:40px;background:var(--gold);transform:skewX(-12deg);text-align:center}
  .ribbon span{display:block;transform:skewX(12deg);font-family:"Oswald",sans-serif;font-weight:700;font-size:24px;line-height:40px;color:var(--white)}
  .contact{left:400px;width:400px;top:598px;text-align:center;color:var(--white);font-size:15px;line-height:24px}
  .contact svg{vertical-align:-2px;margin-right:6px}

  /* Right panel */
  .cover-brand{left:800px;width:400px;top:92px;display:flex;align-items:center;justify-content:center;gap:12px}
  .cover-brand .sq{width:38px;height:38px;border:5px solid var(--navy)}
  .cover-brand .name{font-family:"Open Sans",sans-serif;font-weight:700;font-size:24px;color:var(--navy)}
  .solution{left:800px;width:400px;top:588px;text-align:center;font-family:"Oswald",sans-serif;font-weight:700;text-transform:uppercase}
  .solution .l1{font-size:34px;line-height:40px;color:var(--white)}
  .solution .l2{display:inline-block;margin-top:4px;padding:0 18px;background:var(--gold);transform:skewX(-12deg);font-size:30px;line-height:40px;color:var(--white)}
  .solution .l2 span{display:inline-block;transform:skewX(12deg)}
  .serving{left:800px;width:400px;top:690px;text-align:center;font-weight:600;font-size:15px;line-height:20px;color:var(--white)}
  .rule{left:880px;top:740px;width:240px;height:1px;background:var(--gold)}
  .web{left:800px;width:400px;top:752px;text-align:center;font-size:15px;letter-spacing:4px;color:var(--white)}
  .web b{color:var(--gold);font-weight:600}
</style>
</head>
<body>
<main class="brochure">

  <svg class="panel-shapes" width="1200" height="800" viewBox="0 0 1200 800">
    <defs>
      <linearGradient id="goldFill" x1="0" y1="0" x2="1" y2="1">
        <stop offset="0" stop-color="#e3bf80"/><stop offset="1" stop-color="#cfa35c"/>
      </linearGradient>
      <linearGradient id="cabinetTones" x1="0" y1="0" x2="1" y2="1">
        <stop offset="0" stop-color="#f1eee8"/><stop offset=".5" stop-color="#b89a74"/><stop offset="1" stop-color="#e8e5df"/>
      </linearGradient>
      <linearGradient id="stairTones" x1="0" y1="0" x2="0" y2="1">
        <stop offset="0" stop-color="#ece9e3"/><stop offset=".6" stop-color="#7d6350"/><stop offset="1" stop-color="#d9d5cf"/>
      </linearGradient>
      <radialGradient id="studioGrey" cx=".5" cy=".45" r=".7">
        <stop offset="0" stop-color="#f4f4f4"/><stop offset="1" stop-color="#bdbdbd"/>
      </radialGradient>
    </defs>

    <!-- Left panel -->
    <rect x="0" y="0" width="400" height="800" fill="url(#goldFill)"/>
    <polygon points="0,0 175,0 250,120 0,260" fill="var(--navy)"/>
    <polygon points="330,270 400,250 400,520 300,470" fill="var(--navy)"/>
    <circle cx="190" cy="250" r="172" fill="url(#cabinetTones)" stroke="var(--white)" stroke-width="6" role="img" aria-label="Photo of kitchen cabinets prepped and masked for painting"/>

    <!-- Middle panel -->
    <rect x="400" y="0" width="400" height="800" fill="var(--gold)"/>
    <path d="M400,0 H800 V200 Q600,250 400,230 Z" fill="url(#stairTones)" role="img" aria-label="Photo of stairs during tread installation"/>
    <path d="M400,430 Q600,470 800,400 V800 H400 Z" fill="var(--navy)"/>
    <circle cx="450" cy="150" r="115" fill="url(#stairTones)" stroke="var(--white)" stroke-width="6" role="img" aria-label="Photo of completed stairs with new wood treads"/>
    <line x1="470" y1="378" x2="575" y2="378" stroke="var(--white)" stroke-width="1.5"/>
    <line x1="625" y1="378" x2="730" y2="378" stroke="var(--white)" stroke-width="1.5"/>
    <circle cx="600" cy="378" r="15" fill="var(--navy)" stroke="var(--white)" stroke-width="2"/>
    <path d="M594,371 q-2,7 5,13 q7,5 10,1 l-3,-3 q-2,2 -4,0 q-3,-3 -3,-5 q2,-1 0,-4 z" fill="var(--white)"/>

    <!-- Right panel -->
    <rect x="800" y="0" width="400" height="800" fill="url(#studioGrey)"/>
    <path d="M800,0 H1200 V150 Q1000,215 800,190 Z" fill="var(--paper)"/>
    <rect x="860" y="200" width="280" height="340" fill="url(#studioGrey)" role="img" aria-label="Photo of a handyman in a hard hat holding many tools"/>
    <path d="M800,560 Q1000,600 1200,500 V800 H800 Z" fill="var(--navy)"/>

    <!-- Fold lines -->
    <line x1="400" y1="0" x2="400" y2="800" stroke="rgba(0,0,0,.08)" stroke-width="1"/>
    <line x1="800" y1="0" x2="800" y2="800" stroke="rgba(0,0,0,.08)" stroke-width="1"/>
  </svg>

  <!-- Left panel text -->
  <h2 class="abs headline">
    <span class="w">Fix it.</span><br>
    <span class="n">Repair it.</span><br>
    <span class="w">Change it.</span><br>
    <span class="n">Build it.</span>
  </h2>
  <ul class="abs perks">
    <li>35 years Experience</li>
    <li>Free Written Estimates</li>
    <li>Fully Insured</li>
    <li>Locally Owned</li>
    <li>Prompt Response</li>
  </ul>

  <!-- Middle panel text -->
  <div class="abs call"><div class="l1">One Call</div><div class="l2">Does it All</div></div>
  <div class="abs phone-bar">(555) 014-2876</div>
  <div class="abs brand-mark"><span class="sq"></span><span class="name">TWR Handyman Services</span></div>
  <div class="abs ribbon"><span>TWR Handyman Services</span></div>
  <address class="abs contact" style="font-style:normal">
    <div><svg width="12" height="14" viewBox="0 0 12 14"><path d="M6,0 a5,5 0 0 1 5,5 c0,4 -5,9 -5,9 s-5,-5 -5,-9 a5,5 0 0 1 5,-5z" fill="var(--gold)"/><circle cx="6" cy="5" r="2" fill="var(--navy)"/></svg>48 Cedar Mill Rd</div>
    <div>Westbrook, Maine 04092</div>
    <div><svg width="14" height="10" viewBox="0 0 14 10"><rect x=".5" y=".5" width="13" height="9" fill="none" stroke="var(--white)"/><path d="M.5,.5 L7,6 L13.5,.5" fill="none" stroke="var(--white)"/></svg>tom@twrhandyman.com</div>
    <div><svg width="12" height="12" viewBox="0 0 12 12"><circle cx="6" cy="6" r="5.3" fill="none" stroke="var(--white)"/><line x1=".7" y1="6" x2="11.3" y2="6" stroke="var(--white)"/><ellipse cx="6" cy="6" rx="2.3" ry="5.3" fill="none" stroke="var(--white)"/></svg>www.twrhandyman.com</div>
  </address>

  <!-- Right panel text -->
  <div class="abs cover-brand"><span class="sq"></span><span class="name">TWR Handyman Services</span></div>
  <div class="abs solution">
    <div class="l1">We are the solution</div>
    <div class="l2"><span>To your problems!</span></div>
  </div>
  <p class="abs serving">Serving Southern Maine For all Your<br>Painting &amp; Remodeling Needs</p>
  <div class="abs rule"></div>
  <p class="abs web">www.<b>TWRHandyman</b>.com</p>

</main>
</body>
</html>
```